This book will apply the 12 Steps to gaming addiction, also known as video game addiction. The primary purpose of the book is to provide an effective solution for this new type of addiction. The solution is based on the rich and successful concepts of traditional twelve-step programs like RL.

The title on the cover will be "Nine Doors Past the Glowing Screen" and "by Martin Quorby". A subtitle can be used if it works in your design of "A Practical Path Beyond Compulsive Console Play". Cover will be for a 6" x 9" book approximately 110 pages in length.

Some back cover text including some review quotes and an author bio are in the attached Word doc. There is also an author photo attached for for the back cover.

Requirements
Must have
• For the cover design it could be stylized, or an image, a partial image, or whatever. I am open to suggestions. Think about what would be noticed by a person searching for help with moderating their video game use, or by the parents or loved ones of problem gamers. Something contemporary and eye catching.

```html
<!DOCTYPE html>
<html lang="en">
<head>
<meta charset="utf-8">
<title>Nine Doors Past the Glowing Screen — Back Cover</title>
<link rel="stylesheet" href="https://fonts.googleapis.com/css2?family=Fira+Sans+Extra+Condensed:wght@300;400;600&display=swap">
<style>
  :root {
    --night: #05060f;
    --navy: #0d1230;
    --panel: rgba(6, 8, 20, 0.78);
    --ink: #f2f2f6;
    --lavender: #c9c4ee;
    --rule: #d8d8e4;
    --photo-a: #6f7f4a;
    --photo-b: #2a2f3c;
  }
  * { margin: 0; padding: 0; box-sizing: border-box; }
  html, body { width: 800px; height: 1200px; overflow: hidden; background: var(--night); }
  .back-cover {
    position: relative;
    width: 800px;
    height: 1200px;
    overflow: hidden;
    background:
      radial-gradient(ellipse 420px 520px at 560px 420px, rgba(42, 58, 140, 0.55), transparent 70%),
      linear-gradient(180deg, var(--navy) 0%, var(--night) 100%);
    font-family: "Fira Sans Extra Condensed", "Arial Narrow", sans-serif;
    font-weight: 300;
    color: var(--ink);
  }
  .screen-glow {
    position: absolute;
    left: -20px; top: 20px;
    width: 360px; height: 440px;
    background:
      radial-gradient(ellipse 120px 150px at 190px 130px, rgba(120, 130, 220, 0.55), transparent 70%),
      radial-gradient(ellipse 170px 230px at 160px 210px, rgba(90, 31, 74, 0.45), transparent 75%),
      radial-gradient(ellipse 180px 220px at 200px 220px, rgba(42, 58, 140, 0.5), transparent 80%);
    filter: blur(6px);
  }
  .praise-panel {
    position: absolute;
    left: 100px; top: 104px;
    width: 276px; height: 1008px;
    background: var(--panel);
  }
  .praise-heading {
    position: absolute;
    left: 100px; top: 122px;
    width: 276px;
    text-align: center;
  }
  .praise-heading .lead {
    font-weight: 600;
    font-size: 29px;
    letter-spacing: 0.5px;
    color: var(--lavender);
    line-height: 1;
  }
  .praise-heading .book-title {
    font-weight: 600;
    font-size: 33px;
    line-height: 38px;
    color: var(--ink);
    text-transform: uppercase;
    letter-spacing: 0.5px;
    margin-top: 14px;
  }
  .reviews {
    position: absolute;
    left: 116px; top: 316px;
    width: 241px;
  }
  .review-quote {
    font-size: 16.6px;
    line-height: 21.4px;
    text-align: justify;
  }
  .review-credit {
    text-align: right;
    font-size: 13.8px;
    line-height: 19px;
    margin-top: 12px;
  }
  .review-credit .name { font-weight: 600; color: var(--lavender); display: block; }
  .divider {
    width: 183px;
    height: 1px;
    background: var(--rule);
    margin: 22px auto 24px 27px;
  }
  .blurb {
    position: absolute;
    left: 403px; top: 121px;
    width: 296px;
    font-size: 16.6px;
    line-height: 21.4px;
  }
  .blurb p + p { margin-top: 21px; }
  .blurb .divider-right {
    width: 228px;
    height: 1px;
    background: var(--rule);
    margin: 24px 0 22px 4px;
  }
  .about-heading {
    font-weight: 600;
    font-size: 26px;
    color: var(--lavender);
    line-height: 1;
    margin-bottom: 12px;
    margin-left: 2px;
  }
  .author-photo {
    float: left;
    width: 171px;
    height: 190px;
    margin: 2px 10px 4px 2px;
    border-radius: 8px;
    background: linear-gradient(160deg, var(--photo-a) 0%, #4b5640 45%, var(--photo-b) 100%);
  }
  .bio { font-size: 16.6px; line-height: 21.4px; }
</style>
</head>
<body>
<main class="back-cover">
  <div class="screen-glow" role="img" aria-label="Blurred glowing screen and gamer silhouette in blue and red light"></div>
  <div class="praise-panel"></div>

  <header class="praise-heading">
    <div class="lead">PRAISE FOR</div>
    <div class="book-title">Nine Doors Past<br>the Glowing<br>Screen</div>
  </header>

  <section class="reviews">
    <p class="review-quote">“A must-read for anyone who is addicted to or thinks they may have a problem with digital gaming. This eloquent work will also be useful to academics and clinicians exploring potential solutions. The author recognizes the similarities between gaming addiction and other addictions, and logically applies one of the most effective known solutions for addiction - The Twelve Steps.”</p>
    <p class="review-credit"><span class="name">- Dale Wrenfield</span>Noted Interventionist and Keynote Speaker</p>

    <div class="divider"></div>

    <p class="review-quote">“If you suffer from digital gaming addiction, I strongly encourage you to use this book as your road map to get you back to the real world.”</p>
    <p class="review-credit"><span class="name">- Owen Barcliff</span>Founder of Signal Desk Review.</p>

    <div class="divider"></div>

    <p class="review-quote">”As a high school teacher for 24 years, husband, father, coach, and 12-Step member, I can assure you that this book will transform the life of anyone who is addicted to video games. Well written, easy to understand, and a wonderful book that will provide you with a clear road map to recovery, and this includes teenagers, a group I have been working with in the classroom for decades.”</p>
    <p class="review-credit"><span class="name">- Luis Marrow</span>Harbor Vale, CA High School Teacher.</p>
  </section>

  <section class="blurb">
    <p>An effective solution to the challenge of Digital Gaming Addiction (aka Video Game Addiction) based on the rich and successful tradition of the Twelve Steps.</p>
    <p>Addiction to Digital Gaming is a new and troubling phenomenon that has burst upon an unprepared society with alarming speed. Many people crave the use of Digital Games in a strikingly similar way to any other addict. Digital Games are a complex software and hardware system that have been designed to promote continued and progressive usage. This sophisticated technology clearly feeds on natural addictive tendencies.</p>
    <p>The 12 Steps are one of the most effective methods for treating addiction in human history. Originating with Recovery League in 1939, the 12 Steps have since been used to treat a variety of other addictions, including drugs, sex, gambling, eating disorders, and many others. Now in this groundbreaking work the 12 Steps are applied to the complex and evolving contemporary phenomenon of Digital Gaming Addiction.</p>
    <div class="divider-right"></div>
    <h2 class="about-heading">About the Author</h2>
    <p class="bio"><span class="author-photo" role="img" aria-label="Portrait photo of the author outdoors"></span>Martin Quorby is a Technology Consultant and Writer with many years of professional coding and consulting experience. He also struggled with addiction to drugs and alcohol and is now clean and sober in a Twelve-Step program for over 17 years. This unique combination of 12-Step experience and technology expertise led him to create Nine Doors Past the Glowing Screen.</p>
  </section>
</main>
</body>
</html>
```